Banner Ad Design Project: Image banner for new website

Hi,

we need an image banner for a new website we just launched. The image banner should come in the formats 728x90 and 300x250.

The website the banner should advertise is http://www.tonal-blender.example/ .

We leave it up to your experience to find the best text and to obtain a great clickrate. Banner should be CATCHY and MOTIVATE people to enter. We do not want to include our current "logo". Will require all design files and fonts.

Best regards,
Ravindra

```html
<!DOCTYPE html>
<html lang="en">
<head>
<meta charset="utf-8">
<title>Tonal Blender banners</title>
<link rel="stylesheet" href="https://fonts.googleapis.com/css2?family=Alegreya:ital@1&family=Cinzel:wght@500&display=swap">
<style>
  :root {
    --stage: #000000;
    --panel-top: #ffffff;
    --panel-bottom: #ebebeb;
    --ink: #2a2a2a;
    --band-dark: #6e6e6e;
    --band-light: #b9b9b9;
    --forest-deep: #3e5a1c;
    --forest-mid: #7c9a3a;
    --forest-light: #e6efc7;
    --sky-deep: #2f4fae;
    --sky-mid: #6f8fd6;
    --sky-light: #e4ecf8;
    --url-ink: #ffffff;
  }
  html, body {
    margin: 0;
    padding: 0;
    width: 1200px;
    height: 857px;
    overflow: hidden;
    background: var(--stage);
  }
  .stage {
    position: relative;
    width: 1200px;
    height: 857px;
  }
  .banner {
    position: absolute;
    top: 218px;
    width: 452px;
    height: 377px;
    overflow: hidden;
  }
  .banner--listen { left: 137px; }
  .banner--create { left: 637px; }
  .banner__photo {
    position: absolute;
    inset: 0;
  }
  .banner--listen .banner__photo {
    background: linear-gradient(100deg, var(--forest-deep) 0%, var(--forest-mid) 55%, var(--forest-light) 100%);
  }
  .banner--create .banner__photo {
    background: linear-gradient(160deg, var(--sky-light) 0%, var(--sky-mid) 45%, var(--sky-deep) 100%);
  }
  .banner__panel {
    position: absolute;
    inset: 0;
    width: 452px;
    height: 377px;
  }
  .banner__headline {
    position: absolute;
    top: 44px;
    left: 0;
    width: 100%;
    margin: 0;
    text-align: center;
    font-family: "Alegreya", Georgia, serif;
    font-style: italic;
    font-weight: 400;
    font-size: 45px;
    line-height: 57px;
    color: var(--ink);
  }
  .banner__cta {
    position: absolute;
    top: 189px;
    left: 129px;
    width: 164px;
    height: 49px;
    box-sizing: border-box;
    border: 1.5px dashed var(--ink);
    border-radius: 12px;
    display: flex;
    align-items: center;
    justify-content: center;
    font-family: "Cinzel", "Times New Roman", serif;
    font-weight: 500;
    font-size: 24px;
    letter-spacing: 0.5px;
    color: var(--ink);
    text-decoration: none;
  }
  .banner__url {
    position: absolute;
    top: 344px;
    left: 86px;
    margin: 0;
    font-family: "Alegreya", Georgia, serif;
    font-style: italic;
    font-size: 20px;
    color: var(--url-ink);
  }
  .banner--create .banner__url { color: var(--ink); }
</style>
</head>
<body>
<main class="stage">

  <section class="banner banner--listen">
    <div class="banner__photo" role="img" aria-label="Sunlit green forest with tall trees"></div>
    <svg class="banner__panel" viewBox="0 0 452 377" aria-hidden="true">
      <defs>
        <linearGradient id="panel-fill-a" x1="0" y1="0" x2="0" y2="1">
          <stop offset="0" stop-color="var(--panel-top)"/>
          <stop offset="1" stop-color="var(--panel-bottom)"/>
        </linearGradient>
        <linearGradient id="band-fill-a" x1="0" y1="0" x2="1" y2="0">
          <stop offset="0" stop-color="var(--band-light)"/>
          <stop offset="1" stop-color="var(--band-dark)"/>
        </linearGradient>
      </defs>
      <path d="M0 0 H452 V214 C380 240 250 300 120 296 C70 294 30 282 0 270 Z" fill="url(#band-fill-a)"/>
      <path d="M0 0 H452 V204 C380 232 250 290 120 290 C70 289 30 279 0 268 Z" fill="url(#panel-fill-a)"/>
    </svg>
    <h2 class="banner__headline">Listen online to<br>relaxing sounds</h2>
    <a class="banner__cta" href="http://www.tonal-blender.example/">Try now</a>
    <p class="banner__url">www.tonal-blender.example</p>
  </section>

  <section class="banner banner--create">
    <div class="banner__photo" role="img" aria-label="Blue sky with wispy white clouds and sun rays"></div>
    <svg class="banner__panel" viewBox="0 0 452 377" aria-hidden="true">
      <defs>
        <linearGradient id="panel-fill-b" x1="0" y1="0" x2="0" y2="1">
          <stop offset="0" stop-color="var(--panel-top)"/>
          <stop offset="1" stop-color="var(--panel-bottom)"/>
        </linearGradient>
        <linearGradient id="band-fill-b" x1="0" y1="0" x2="1" y2="0">
          <stop offset="0" stop-color="var(--band-light)"/>
          <stop offset="1" stop-color="var(--band-dark)"/>
        </linearGradient>
      </defs>
      <path d="M0 0 H452 V214 C380 240 250 300 120 296 C70 294 30 282 0 270 Z" fill="url(#band-fill-b)"/>
      <path d="M0 0 H452 V204 C380 232 250 290 120 290 C70 289 30 279 0 268 Z" fill="url(#panel-fill-b)"/>
    </svg>
    <h2 class="banner__headline" style="top:36px">Create your own<br>ambient atmosphere</h2>
    <a class="banner__cta" href="http://www.tonal-blender.example/">Try now</a>
    <p class="banner__url">www.tonal-blender.example</p>
  </section>

</main>
</body>
</html>
```